Perfect — here’s the updated version of your description with **title #1** and the integration/booking functionality references removed, while still keeping the “motivation to book” idea in the design style:
---
**Luxury Property Website Design – Dominican Republic**
We are looking to create a professional and visually appealing **website design** for a premium property that we will be promoting as a short-term rental.
The property is located in an **exclusive area of the Dominican Republic** and offers a high-end experience for guests. Our goal is to create a website that highlights the **luxury, comfort, and exclusivity** of the property, while motivating visitors to **make a reservation inquiry**.
**Key Requirements:**
* A clean, modern, and elegant design that reflects the **premium nature** of the property.
* High-quality visual presentation of the **property’s best features** (rooms, amenities, location, views, nearby attractions).
* Easy-to-navigate structure
* Mobile-friendly and optimized for all screen sizes.
* Space for testimonials or guest reviews to build trust.
**Design Style We Like:**
* Elegant and sophisticated, with a touch of tropical luxury.
* Use of high-quality photography, subtle animations, and a warm color palette that reflects the Caribbean atmosphere.
* A premium feel, similar to boutique hotel or luxury villa rental websites.
**Deliverables:**
* Homepage design.
* Property detail page design (with gallery, amenities, and booking inquiry section).
Contact page or About Us page
* Photo Gallery
The final design should capture the essence of a **luxury getaway** and make visitors feel compelled to reserve their night.

```html
<!DOCTYPE html>
<html lang="en">
<head>
<meta charset="utf-8">
<title>Costa Serena Vista Alta 43</title>
<link href="https://fonts.googleapis.com/css2?family=Inter:wght@400;500;600;700;800&display=swap" rel="stylesheet">
<style>
:root{
  --accent:#ee7d1c;
  --accent-soft:#fdf1e4;
  --navy:#0e1a2f;
  --ink:#1c2230;
  --muted:#6b7280;
  --line:#e6e8ec;
  --bg-soft:#f4f5f7;
  --white:#fff;
}
*{box-sizing:border-box;margin:0;padding:0}
html,body{width:1200px;height:2740px;overflow:hidden}
body{font-family:'Inter',sans-serif;color:var(--ink);background:var(--white);position:relative}
.hero{position:absolute;left:0;top:0;width:1200px;height:410px;background:linear-gradient(180deg,#2b6aa5 0%,#4f95c4 40%,#3d7b5c 75%,#1f3d33 100%)}
.hero::after{content:"";position:absolute;inset:0;background:linear-gradient(90deg,rgba(10,20,35,.55),rgba(10,20,35,.1))}
.nav{position:absolute;top:0;left:0;right:0;height:48px;display:flex;align-items:center;padding:0 70px;z-index:2}
.brand{color:var(--accent);font-weight:700;font-size:16px}
.nav ul{list-style:none;display:flex;gap:22px;margin-left:auto;margin-right:22px}
.nav li{color:#fff;font-size:12px;font-weight:500}
.btn{background:var(--accent);color:#fff;border-radius:5px;font-weight:600;font-size:11px;padding:8px 14px;display:inline-block}
.hero-text{position:absolute;left:90px;top:225px;z-index:2;color:#fff}
.hero-text h1{font-size:46px;font-weight:800;letter-spacing:-.5px}
.hero-text h1 span{color:var(--accent)}
.hero-text p{font-size:15px;margin-top:12px;opacity:.92}
.badges{display:flex;gap:18px;margin-top:14px;font-size:12px;opacity:.85}
.section{position:absolute;left:90px}
h2{font-size:24px;font-weight:700}
.lead{font-size:13.5px;line-height:1.6;color:#4b5160;margin-top:14px;width:710px}
.stars{position:absolute;left:520px;top:6px;color:#f4b400;font-size:13px}
.stars small{color:var(--muted);font-size:11px}
.features{display:grid;grid-template-columns:1fr 1fr;gap:20px;margin-top:26px;width:710px}
.feat{border-radius:8px;padding:22px;height:165px}
.feat .ic{width:34px;height:34px;border-radius:8px;background:#fff;display:flex;align-items:center;justify-content:center;color:var(--accent);font-weight:700}
.feat h3{font-size:15px;margin-top:16px}
.feat p{font-size:11.5px;color:var(--muted);margin-top:6px;line-height:1.5}
.booking{position:absolute;left:905px;top:468px;width:210px;height:555px;border:1px solid var(--line);border-radius:10px;padding:20px;box-shadow:0 6px 18px rgba(0,0,0,.06)}
.price{text-align:center;font-size:26px;font-weight:800}
.price small{font-size:11px;color:var(--muted);font-weight:400}
.booking .rate{text-align:center;color:#f4b400;font-size:11px;margin-top:4px}
.field-row{display:flex;gap:8px;margin-top:18px}
.field{flex:1}
.field label{font-size:10px;color:var(--muted)}
.field .in{border:1px solid var(--line);border-radius:4px;height:30px;margin-top:4px;font-size:10px;padding:8px;color:#999}
.reserve{display:block;text-align:center;margin-top:18px;padding:12px}
.note{font-size:9px;color:var(--muted);text-align:center;margin-top:8px;line-height:1.4}
.assist{border-top:1px solid var(--line);margin-top:20px;padding-top:16px;font-size:11px}
.assist b{display:block;margin-bottom:10px}
.assist div{margin:7px 0;color:#4b5160;display:flex;gap:8px;align-items:center}
.assist i{width:8px;height:8px;border-radius:50%;background:var(--accent);display:inline-block}
.rooms{display:flex;gap:20px;margin-top:20px;width:710px}
.room{flex:1;border:1px solid var(--line);border-radius:8px;padding:18px;height:110px}
.room h4{font-size:14px;display:flex;gap:8px;align-items:center}
.room h4::before{content:"";width:16px;height:12px;border-radius:3px;background:var(--accent)}
.room p{font-size:11.5px;color:var(--muted);margin-top:8px;line-height:1.5}
.amen{display:grid;grid-template-columns:1fr 1fr;column-gap:40px;row-gap:16px;margin-top:22px;width:560px;font-size:12px;color:#4b5160}
.amen div{display:flex;gap:8px;align-items:center}
.amen div::before{content:"✓";color:var(--accent);font-weight:700}
.gallery-band{position:absolute;left:0;top:1520px;width:1200px;height:320px;background:var(--bg-soft)}
.gal-head{position:absolute;left:90px;top:1585px;width:1020px;display:flex;align-items:center}
.outline{margin-left:auto;border:1px solid var(--accent);color:var(--accent);background:#fff}
.photos{position:absolute;left:90px;top:1645px;display:flex;gap:14px}
.photo{width:245px;height:160px;border-radius:6px}
.loc-item{display:flex;gap:14px;margin-top:30px}
.loc-item .ic{width:28px;height:28px;border-radius:6px;background:var(--accent-soft);flex:none}
.loc-item h5{font-size:13px}
.loc-item p{font-size:11px;color:var(--muted);margin-top:4px;line-height:1.5}
.map{position:absolute;left:700px;top:1915px;width:410px;height:210px;background:#ebedf0;border-radius:8px}
footer{position:absolute;left:0;top:2440px;width:1200px;height:300px;background:var(--navy);color:#c7cbd3}
.fcol{position:absolute;top:36px;font-size:11px;line-height:1.7}
.fcol h6{color:#fff;font-size:12px;margin-bottom:8px}
.social{display:flex;gap:8px;margin-top:14px}
.social span{width:20px;height:20px;border-radius:50%;background:var(--accent)}
.copy{position:absolute;left:0;right:0;bottom:24px;text-align:center;font-size:10px;color:#8891a0;border-top:1px solid #23304a;padding-top:18px;margin:0 90px}
</style>
</head>
<body>
<header class="hero" role="img" aria-label="Luxury villa with pool, palm trees and tropical sky at dusk">
  <nav class="nav">
    <div class="brand">Costa Serena</div>
    <ul><li>Home</li><li>Property</li><li>Gallery</li><li>About</li><li>Contact</li></ul>
    <span class="btn">Book Now</span>
  </nav>
  <div class="hero-text">
    <h1>Costa Serena <span>Vista Alta 43</span></h1>
    <p>Luxury 4-bedroom villa with private pool and golf course views</p>
    <div class="badges"><span>4 Bedrooms</span><span>4.5 Baths</span><span>Sleeps 10</span><span>Private Pool</span></div>
  </div>
</header>

<section class="section" style="top:470px">
  <h2>Property Overview</h2>
  <div class="stars">★★★★★ <small>(24 reviews)</small></div>
  <p class="lead">Experience the epitome of Caribbean luxury at Costa Serena Vista Alta 43. This stunning 4-bedroom villa offers unparalleled elegance and comfort in one of the Dominican Republic's most prestigious resort communities. With breathtaking ocean views, world-class amenities, and exclusive access to the renowned Vista Alta Golf Course, every moment of your stay promises to be extraordinary.</p>
  <div class="features">
    <div class="feat" style="background:#fdf3e4"><div class="ic">⌂</div><h3>Spacious Living</h3><p>4 luxurious bedrooms, 4.5 bathrooms, open-plan living and dining areas</p></div>
    <div class="feat" style="background:#eaf3fc"><div class="ic">≈</div><h3>Private Pool</h3><p>Infinity pool with ocean views, outdoor terrace and dining area</p></div>
    <div class="feat" style="background:#e9f7ee"><div class="ic">✦</div><h3>Gourmet Kitchen</h3><p>Fully equipped with premium appliances and elegant finishes</p></div>
    <div class="feat" style="background:#f2eefc"><div class="ic">◎</div><h3>Golf Access</h3><p>Direct access to Marco Alvez's world-renowned golf courses</p></div>
  </div>
</section>

<aside class="booking">
  <div class="price">$850 <small>/ night</small></div>
  <div class="rate">★★★★★ <span style="color:#6b7280">4.9 (24 reviews)</span></div>
  <div class="field-row">
    <div class="field"><label>Check-in</label><div class="in">mm/dd</div></div>
    <div class="field"><label>Check-out</label><div class="in">mm/dd</div></div>
  </div>
  <div class="field" style="margin-top:12px"><label>Guests</label><div class="in">4 Guests</div></div>
  <span class="btn reserve">Reserve Now</span>
  <p class="note">Free cancellation up to 48 hours before check-in</p>
  <div class="assist">
    <b>Need Assistance?</b>
    <div><i></i>+1 (809) 555-0148</div>
    <div><i></i>stay@costaserena43.com</div>
    <div><i></i>24/7 Concierge Available</div>
  </div>
</aside>

<section class="section" style="top:1165px">
  <h2 style="font-size:20px">Room Configuration</h2>
  <div class="rooms">
    <div class="room"><h4>Master Suite</h4><p>King bed, ocean view, private balcony, en-suite bathroom with jacuzzi</p></div>
    <div class="room"><h4>Guest Bedrooms</h4><p>3 elegant bedrooms with queen beds, garden views, private bathrooms</p></div>
  </div>
</section>

<section class="section" style="top:1265px;margin-top:0">
</section>

<section class="section" style="top:1345px">
  <h2 style="font-size:20px">Villa Amenities</h2>
  <div class="amen" style="row-gap:12px">
    <div>Air conditioning throughout</div><div>Private parking</div>
    <div>High-speed WiFi</div><div>Daily housekeeping</div>
    <div>Flat-screen TVs in all rooms</div><div>Concierge services</div>
    <div>Premium sound system</div><div>24/7 security</div>
    <div>Wine cooler &amp; bar area</div><div>Golf cart included</div>
  </div>
</section>

<div class="gallery-band"></div>
<div class="gal-head"><h2 style="font-size:22px">Property Gallery</h2><span class="btn outline">View All 24 Photos</span></div>
<div class="photos">
  <div class="photo" role="img" aria-label="Pool terrace overlooking the sea" style="background:linear-gradient(135deg,#5fa3c9,#c9a777)"></div>
  <div class="photo" role="img" aria-label="Bright living room" style="background:linear-gradient(135deg,#e9dccb,#a88b6c)"></div>
  <div class="photo" role="img" aria-label="Master bedroom with ocean view" style="background:linear-gradient(135deg,#d8cfc2,#7b8fa3)"></div>
  <div class="photo" role="img" aria-label="Villa pool lit at night" style="background:linear-gradient(135deg,#1e3a5f,#3b8fb5)"></div>
</div>

<section class="section" style="top:1920px">
  <h2>Prime Location</h2>
  <p class="lead" style="width:500px">Located within the exclusive Costa Serena resort in the Dominican Republic, this premier destination offers world-class amenities and attractions just minutes from your villa.</p>
  <div class="loc-item"><span class="ic"></span><div><h5>Vista Alta Golf Course</h5><p>Direct access to Marco Alvez's masterpiece featuring clifftop holes and ocean views</p></div></div>
  <div class="loc-item"><span class="ic"></span><div><h5>Marina &amp; Beach</h5><p>Private marina with yacht charters and the pristine Palmera Cove - 5 minutes away</p></div></div>
  <div class="loc-item"><span class="ic"></span><div><h5>Villa Mirador</h5><p>Historic replica village with artisan shops and amphitheater - 10 minutes drive</p></div></div>
  <div class="loc-item"><span class="ic"></span><div><h5>Airport Access</h5><p>Regional Airport - 15 minutes, International Airport - 30 minutes</p></div></div>
</section>
<div class="map" role="img" aria-label="Area map of the resort and nearby attractions"></div>

<footer>
  <div class="fcol" style="left:90px;width:330px">
    <div class="brand" style="font-size:17px;margin-bottom:8px">Costa Serena Vista Alta 43</div>
    Experience luxury and tranquility in one of the most exclusive areas of the Dominican Republic. Your perfect tropical getaway awaits with world-class amenities and breathtaking views.
    <div class="social"><span></span><span></span><span></span></div>
  </div>
  <div class="fcol" style="left:612px"><h6>Quick Links</h6>Home<br>Property Details<br>Photo Gallery<br>About Us</div>
  <div class="fcol" style="left:872px"><h6>Contact</h6>+1 (809) 555-0148<br>hello@costaserena43.com<br>Costa Serena,<br>Dominican Republic</div>
  <div class="copy">© 2024 Costa Serena Vista Alta 43. All rights reserved.</div>
</footer>
</body>
</html>
```